Wedding invitations

We are looking for fresh wedding invitation designs
NO COPYRIGHTED MATERIAL

I will post examples of fiances likes as available
The winner is not only guaranteed the prize but will also be offered a position on our staff.

Please don't just post random artwork. Please look at other wedding invitations on the web
We like the classic styles
We will need the final winner to send us the entry in PSD format

Below are links to a few we like for ideas and sizes:
http://www.quillmerry.com/p-51937-pale-ivory-glimmer-filigree-trim-regalia.aspx
http://www.quillmerry.com/p-208615-misty-grace-pewter.aspx
http://www.quillmerry.com/p-209384-airy-opulent-fold.aspx
http://www.quillmerry.com/p-63159-grand-curlo-v-sleeve-with-gilt.aspx
http://www.quillmerry.com/p-47293-rose-z-panel-with-wavy-border-and-gauze-banding.aspx

```html
<!DOCTYPE html>
<html lang="en">
<head>
<meta charset="utf-8">
<title>Wedding Invitation – Clara &amp; Rafael</title>
<link rel="stylesheet" href="https://fonts.googleapis.com/css2?family=Cinzel:wght@400;700&display=swap">
<style>
  :root {
    --frame: #d0e6ee;
    --paper: #f9f8f9;
    --accent: #36b0e0;
    --accent-soft: #a9dcf1;
    --accent-light: #7cccec;
    --ink-grey: #8c8c8c;
    --mark-grey: #6f6f6f;
    --white: #ffffff;
  }
  html, body {
    margin: 0;
    padding: 0;
    overflow: hidden;
    background: var(--frame);
  }
  .invitation {
    position: relative;
    width: 828px;
    height: 1200px;
    background: var(--frame);
    overflow: hidden;
    font-family: "Cinzel", "Times New Roman", serif;
  }
  .card {
    position: absolute;
    left: 18px;
    top: 20px;
    width: 790px;
    height: 1162px;
    background: var(--paper);
  }
  .seal {
    position: absolute;
    left: 0;
    top: 0;
    width: 828px;
    height: 400px;
  }
  .line {
    position: absolute;
    left: 0;
    width: 828px;
    margin: 0;
    text-align: center;
    color: var(--ink-grey);
    font-weight: 400;
    line-height: 1;
  }
  .line--small { font-size: 14px; letter-spacing: 0.3px; }
  .line--name {
    font-size: 31px;
    color: var(--accent);
    letter-spacing: 4px;
  }
  .line--venue { font-size: 24px; text-transform: uppercase; }
  .line--quote { font-size: 14px; }
  .quote-mark {
    font-size: 30px;
    font-weight: 700;
    color: var(--mark-grey);
    vertical-align: -8px;
    line-height: 0;
  }
  .line--closing { font-size: 28px; letter-spacing: 0.5px; text-transform: uppercase; }
</style>
</head>
<body>
<main class="invitation">
  <div class="card"></div>

  <svg class="seal" viewBox="0 0 828 400">
    <rect class="seal__flourish" role="img" aria-label="Curled scroll flourish, left side" x="174" y="190" width="110" height="76" rx="38" fill="var(--accent-soft)"/>
    <rect class="seal__flourish" role="img" aria-label="Curled scroll flourish, right side" x="552" y="190" width="110" height="76" rx="38" fill="var(--accent-soft)"/>
    <circle class="seal__disc" role="img" aria-label="Round seal with a dotted ring ornament" cx="416" cy="235" r="138" fill="var(--accent)"/>
    <text x="416" y="172" text-anchor="middle" fill="var(--white)" font-family="Cinzel, serif" font-size="14">THE WEDDING</text>
    <rect class="seal__monogram" role="img" aria-label="Calligraphic monogram of the couple's initials C and R" x="340" y="188" width="152" height="88" rx="30" fill="var(--accent-light)"/>
    <text x="416" y="318" text-anchor="middle" fill="var(--white)" font-family="Cinzel, serif" font-size="14">01.22.14</text>
  </svg>

  <p class="line line--small" style="top:474px">together with their parents</p>
  <h1 class="line line--name" style="top:520px">Clara Joy Medina</h1>
  <p class="line line--small" style="top:592px">and</p>
  <h1 class="line line--name" style="top:633px">Rafael Dominic Santos</h1>

  <p class="line line--small" style="top:708px">request the honor of your presence at their marriage</p>
  <p class="line line--small" style="top:730px">on saturday january 22, 2014 at eight o'clock in the morning</p>

  <p class="line line--venue" style="top:782px">St. Anselm Chapel</p>
  <p class="line line--small" style="top:811px">5678 west linden avenue, marisol city</p>
  <p class="line line--small" style="top:833px">followed by a reception</p>

  <p class="line line--quote" style="top:874px"><span class="quote-mark">“</span> as our love brought a new meaning in our life,</p>
  <p class="line line--quote" style="top:896px">so will our marriage bring a new meaning to love. <span class="quote-mark">”</span></p>

  <p class="line line--closing" style="top:1108px">The Invitation...</p>
</main>
</body>
</html>
```